Criminal Defense Law Firm needs Stationary design Theme for a Business Card, Envelope, and Letterhea

Our Law Firm is seeking a general design concept for a business card, letterhead, and Envelope.

Our website is WillowcrestTrialDesk.com

A design for these three items is requested to keep branding in place for the firm. Would like to keep the Firm Colors on the website consistent with our branding on business cards, letterheads, and mailing envelopes #10 size to be exact.

We would like business cards printed front and back with Law firm Colors from website.

Letterhead with law firm colors as well. Design is not limited to just the header, but the footer can be utilized as well for email, website, phone, fax, etc.

Simple #10 envelope consisting of the same design principles set out in the previous two designs.

```html
<!DOCTYPE html>
<html lang="en">
<head>
<meta charset="utf-8">
<title>Willowcrest Trial Law Offices — Stationery</title>
<link href="https://fonts.googleapis.com/css2?family=Crimson+Pro:wght@400&family=Questrial&display=swap" rel="stylesheet">
<style>
:root{
  --teal:#15acc4;
  --ink:#252525;
  --gold:#a8935f;
  --paper:#ffffff;
  --ground:#ebebeb;
  --faint:#e6e6e6;
  --serif:"Crimson Pro", Georgia, serif;
  --sans:"Questrial", Arial, sans-serif;
}
*{box-sizing:border-box;margin:0;padding:0}
html,body{width:1200px;height:1000px;overflow:hidden;background:var(--ground)}
.canvas{position:relative;width:1200px;height:1000px}
.sheet{position:absolute;background:var(--paper);overflow:hidden}
.band{position:absolute;left:0;right:0}
.teal{background:var(--teal)}
.ink{background:var(--ink)}
.gold{background:var(--gold)}
.brand{position:absolute;display:flex;align-items:center;color:var(--paper);font-family:var(--serif);text-transform:uppercase;line-height:1.05;letter-spacing:.02em}
.brand .mark{border:1.5px solid currentColor;border-radius:50%;flex:none}
.brand.dark{color:var(--ink)}
.watermark{position:absolute;border:5px solid var(--faint);border-radius:50%}
.contact{position:absolute;font-family:var(--sans);color:var(--gold);line-height:1.7}
.contact .row{display:flex;align-items:center;gap:5px}
.contact .phone{width:10px;height:10px;flex:none}
.person{position:absolute;font-family:var(--sans);color:var(--ink);text-transform:uppercase;font-size:8px;letter-spacing:.02em}
</style>
</head>
<body>
<div class="canvas">

  <!-- Letterhead -->
  <section class="sheet letterhead" style="left:102px;top:146px;width:483px;height:687px">
    <div class="band teal" style="top:0;height:18px"></div>
    <div class="band ink" style="top:18px;height:56px"></div>
    <div class="brand" style="left:232px;top:28px;font-size:15.5px;gap:10px">
      <span class="mark" style="width:30px;height:30px"></span>
      <span>Willowcrest Trial<br>Law Offices</span>
    </div>
    <div class="watermark" style="left:128px;top:220px;width:230px;height:250px"></div>
    <div class="band ink" style="top:621px;height:48px"></div>
    <div class="band gold" style="top:669px;height:18px"></div>
    <div class="brand" style="left:30px;top:629px;font-size:11px;gap:8px">
      <span class="mark" style="width:26px;height:26px"></span>
      <span>Willowcrest Trial<br>Law Offices</span>
    </div>
    <div class="contact" style="left:224px;top:630px;font-size:7.5px">
      <div>www.willowcresttrialdesk.com</div>
      <div class="row"><svg class="phone" viewBox="0 0 10 10"><circle cx="5" cy="5" r="5" fill="var(--teal)"/><path d="M3.2 2.6l1 .9-.5.8c.4.8.9 1.3 1.7 1.7l.8-.5.9 1-.6.7C4.6 7 3 5.4 2.6 3.3z" fill="#252525"/></svg>555.014.2270</div>
    </div>
    <div class="contact" style="left:359px;top:630px;font-size:7.5px">
      <div>2210 Alder Street NW,</div>
      <div>Fernhaven, NM 87140</div>
    </div>
  </section>

  <!-- Envelope back -->
  <section class="sheet envelope-back" style="left:624px;top:146px;width:542px;height:259px">
    <svg width="542" height="110" viewBox="0 0 542 110" style="position:absolute;left:0;top:0" aria-hidden="true">
      <path d="M0 0H542L535 40Q532 48 520 50L300 106Q286 110 270 108L22 50Q10 48 7 40Z" fill="var(--teal)"/>
    </svg>
  </section>

  <!-- Envelope front -->
  <section class="sheet envelope-front" style="left:624px;top:427px;width:542px;height:259px">
    <div class="band teal" style="top:0;height:8px"></div>
    <div class="band ink" style="top:8px;height:7px"></div>
    <div class="watermark" style="left:462px;top:120px;width:80px;height:86px;border-width:3px"></div>
    <div class="band ink" style="top:209px;height:40px"></div>
    <div class="band gold" style="top:249px;height:10px"></div>
    <div class="brand" style="left:4px;top:214px;font-size:10.5px;gap:8px">
      <span class="mark" style="width:25px;height:25px"></span>
      <span>Willowcrest Trial<br>Law Offices</span>
    </div>
    <div class="contact" style="left:199px;top:215px;font-size:7.5px">
      <div>www.willowcresttrialdesk.com</div>
      <div class="row"><svg class="phone" viewBox="0 0 10 10"><circle cx="5" cy="5" r="5" fill="var(--teal)"/><path d="M3.2 2.6l1 .9-.5.8c.4.8.9 1.3 1.7 1.7l.8-.5.9 1-.6.7C4.6 7 3 5.4 2.6 3.3z" fill="#252525"/></svg>555.014.2270</div>
    </div>
    <div class="contact" style="left:343px;top:215px;font-size:7.5px">
      <div>2210 Alder Street NW,</div>
      <div>Fernhaven, NM 87140</div>
    </div>
  </section>

  <!-- Business card front -->
  <section class="sheet card-front" style="left:625px;top:706px;width:219px;height:126px">
    <div class="band teal" style="top:0;height:26px"></div>
    <div class="band ink" style="top:26px;height:3px"></div>
    <div class="band ink" style="top:97px;height:3px"></div>
    <div class="band gold" style="top:100px;height:26px"></div>
    <div class="brand dark" style="left:10px;top:45px;font-size:11.5px;gap:10px">
      <span class="mark" style="width:32px;height:32px"></span>
      <span>Willowcrest Trial<br>Law Offices</span>
    </div>
  </section>

  <!-- Business card back -->
  <section class="sheet card-back" style="left:867px;top:706px;width:221px;height:126px">
    <div style="position:absolute;left:0;top:0;width:128px;height:126px;background:var(--ink)"></div>
    <div class="brand" style="left:9px;top:29px;font-size:7px;gap:5px">
      <span class="mark" style="width:18px;height:18px"></span>
      <span>Willowcrest Trial<br>Law Offices</span>
    </div>
    <div class="contact" style="left:11px;top:52px;font-size:6px;line-height:1.9">
      <div>www.willowcresttrialdesk.com</div>
      <div class="row"><svg class="phone" viewBox="0 0 10 10"><circle cx="5" cy="5" r="5" fill="var(--teal)"/><path d="M3.2 2.6l1 .9-.5.8c.4.8.9 1.3 1.7 1.7l.8-.5.9 1-.6.7C4.6 7 3 5.4 2.6 3.3z" fill="#252525"/></svg>555.014.2270</div>
      <div>2210 Alder Street NW,</div>
      <div style="line-height:1">Fernhaven, NM 87140</div>
    </div>
    <div class="person" style="left:138px;top:9px">Marcus Delvane</div>
    <div class="watermark" style="left:132px;top:43px;width:72px;height:78px;border-width:2.5px"></div>
  </section>

</div>
</body>
</html>
```